Parkinson's Disease Progression

Visually describe the rate of Parkinson progression in the first 15 years following diagnosis. Title: "Patient-Perceived Progression of Parkinsonism"

The attached figure names "meanqol" is the curve that should serve as the basis of this graphic. Everything else-- color, labels, font, etc. describe this curve.
Thank you!

Target Market(s)

People with Parkisnon's Disease, neurologists, family members.

Font styles to use
Sans Serif

Requirements
Must have
• Must have the lines going through these exact numbers
Excellent -- 502
Very good- 661
Good- 895
Fair- 1268
Poor- 1655

LABELS:
Title: "Patient-Perceived Progression of Parkinsonism"
"SWI-TC (Self-Logged Wellbeing Index for Tremor Conditions)" should be the label on the left.
"Quality of Life" should be the label on the right
"Years Since Diagnosis" should be the label on the bottom
Nice to have
• A color scheme that goes from GOOD (low numbers) to BAD (high numbers).

Easy to read (elderly)

```html
<!DOCTYPE html>
<html lang="en">
<head>
<meta charset="utf-8">
<title>Patient-Perceived Progression of Parkinsonism</title>
<link rel="stylesheet" href="https://fonts.googleapis.com/css2?family=Oswald:wght@400;500;600&display=swap">
<style>
  :root {
    --navy: #1c1b3c;
    --paper: #ffffff;
    --ink: #111111;
    --accent-red: #ac1f30;
    --muted: #9a9a9a;
    --guide: #cfcfcf;
    --poor: #6a232d;
    --fair: #ac1f30;
    --good: #e77a5e;
    --very-good: #80bf52;
    --excellent: #2a7a1f;
  }
  html, body {
    margin: 0;
    padding: 0;
    width: 1200px;
    height: 820px;
    overflow: hidden;
    background: var(--paper);
  }
  .chart-card {
    display: block;
    width: 1200px;
    height: 820px;
    font-family: "Oswald", sans-serif;
  }
  .title-band { fill: var(--navy); }
  .title { fill: #fff; font-size: 54px; font-weight: 500; letter-spacing: 2px; }
  .axis-line { stroke: var(--ink); stroke-width: 1.2; fill: none; }
  .axis-dot { fill: var(--ink); }
  .tick-label { fill: var(--ink); font-size: 29px; font-weight: 500; }
  .guide { stroke: var(--guide); stroke-width: 1; stroke-dasharray: 5 4; }
  .bar-label { fill: #fff; font-size: 30px; font-weight: 500; letter-spacing: 3px; }
  .value-badge { fill: #fff; }
  .value-text { font-size: 13px; font-weight: 500; text-anchor: middle; }
  .axis-title { fill: var(--accent-red); font-size: 34px; font-weight: 600; letter-spacing: 8px; }
  .side-title { fill: var(--muted); font-size: 34px; font-weight: 500; letter-spacing: 9px; }
</style>
</head>
<body>
<svg class="chart-card" viewBox="0 0 1200 820" xmlns="http://www.w3.org/2000/svg" role="img" aria-label="Bar chart: patient-perceived progression of parkinsonism by quality of life">
  <defs>
    <linearGradient id="grad-poor" x1="0" x2="1"><stop offset="0" stop-color="#3e1218"/><stop offset="0.12" stop-color="var(--poor)"/><stop offset="1" stop-color="var(--poor)"/></linearGradient>
    <linearGradient id="grad-fair" x1="0" x2="1"><stop offset="0" stop-color="#6e1220"/><stop offset="0.12" stop-color="var(--fair)"/><stop offset="1" stop-color="var(--fair)"/></linearGradient>
    <linearGradient id="grad-good" x1="0" x2="1"><stop offset="0" stop-color="#b85a44"/><stop offset="0.12" stop-color="var(--good)"/><stop offset="1" stop-color="var(--good)"/></linearGradient>
    <linearGradient id="grad-very-good" x1="0" x2="1"><stop offset="0" stop-color="#5a8a3a"/><stop offset="0.15" stop-color="var(--very-good)"/><stop offset="1" stop-color="var(--very-good)"/></linearGradient>
    <linearGradient id="grad-excellent" x1="0" x2="1"><stop offset="0" stop-color="#174d10"/><stop offset="0.2" stop-color="var(--excellent)"/><stop offset="1" stop-color="var(--excellent)"/></linearGradient>
  </defs>

  <!-- Title band -->
  <rect class="title-band" x="0" y="0" width="1200" height="113"/>
  <text class="title" x="600" y="78" text-anchor="middle" textLength="1004" lengthAdjust="spacingAndGlyphs">Patient-Perceived Progression of Parkinsonism</text>

  <!-- Guides -->
  <line class="guide" x1="952" y1="202" x2="1026" y2="202"/>
  <line class="guide" x1="808" y1="261" x2="1026" y2="261"/>
  <line class="guide" x1="661" y1="388" x2="1026" y2="388"/>
  <line class="guide" x1="545" y1="482" x2="1026" y2="482"/>
  <line class="guide" x1="429" y1="544" x2="1026" y2="544"/>

  <!-- Bars -->
  <g class="bar bar-poor">
    <path d="M226 179 H938 a22.5 22.5 0 0 1 0 45 H226 Z" fill="url(#grad-poor)"/>
    <text class="bar-label" x="247" y="215">POOR</text>
    <circle class="value-badge" cx="938" cy="202" r="14"/>
    <text class="value-text" x="938" y="207" fill="var(--poor)">1655</text>
  </g>
  <g class="bar bar-fair">
    <path d="M226 238 H793 a22.5 22.5 0 0 1 0 45 H226 Z" fill="url(#grad-fair)"/>
    <text class="bar-label" x="247" y="274">FAIR</text>
    <circle class="value-badge" cx="794" cy="261" r="14"/>
    <text class="value-text" x="794" y="266" fill="var(--fair)">1268</text>
  </g>
  <g class="bar bar-good">
    <path d="M226 366 H648 a22 22 0 0 1 0 44 H226 Z" fill="url(#grad-good)"/>
    <text class="bar-label" x="247" y="401">GOOD</text>
    <circle class="value-badge" cx="647" cy="388" r="14"/>
    <text class="value-text" x="647" y="393" fill="var(--good)">895</text>
  </g>
  <g class="bar bar-very-good">
    <path d="M226 460 H532 a22.5 22.5 0 0 1 0 45 H226 Z" fill="url(#grad-very-good)"/>
    <text class="bar-label" x="247" y="496">VERY GOOD</text>
    <circle class="value-badge" cx="531" cy="482" r="14"/>
    <text class="value-text" x="531" y="487" fill="var(--very-good)">661</text>
  </g>
  <g class="bar bar-excellent">
    <path d="M226 522 H415 a22 22 0 0 1 0 44 H226 Z" fill="url(#grad-excellent)"/>
    <text class="bar-label" x="247" y="557">EXCELLENT</text>
    <circle class="value-badge" cx="415" cy="544" r="14"/>
    <text class="value-text" x="415" y="549" fill="var(--excellent)">502</text>
  </g>

  <!-- Axes -->
  <polyline class="axis-line" points="226,163 226,648 1026,648"/>
  <circle class="axis-dot" cx="226" cy="163" r="5"/>
  <circle class="axis-dot" cx="1026" cy="648" r="5.5"/>

  <g class="y-ticks">
    <line class="axis-line" x1="218" y1="284" x2="226" y2="284"/>
    <line class="axis-line" x1="218" y1="351" x2="226" y2="351"/>
    <line class="axis-line" x1="218" y1="428" x2="226" y2="428"/>
    <line class="axis-line" x1="218" y1="505" x2="226" y2="505"/>
    <line class="axis-line" x1="218" y1="582" x2="226" y2="582"/>
    <text class="tick-label" x="203" y="296" text-anchor="end">1200</text>
    <text class="tick-label" x="203" y="363" text-anchor="end">1000</text>
    <text class="tick-label" x="203" y="440" text-anchor="end">800</text>
    <text class="tick-label" x="203" y="517" text-anchor="end">600</text>
    <text class="tick-label" x="203" y="594" text-anchor="end">400</text>
  </g>

  <g class="x-ticks">
    <line class="axis-line" x1="278" y1="648" x2="278" y2="659"/>
    <line class="axis-line" x1="488" y1="648" x2="488" y2="659"/>
    <line class="axis-line" x1="703" y1="648" x2="703" y2="659"/>
    <line class="axis-line" x1="922" y1="648" x2="922" y2="659"/>
    <text class="tick-label" x="278" y="696" text-anchor="middle">0</text>
    <text class="tick-label" x="488" y="696" text-anchor="middle">5</text>
    <text class="tick-label" x="703" y="696" text-anchor="middle">10</text>
    <text class="tick-label" x="922" y="696" text-anchor="middle">15</text>
  </g>

  <!-- Axis titles -->
  <text class="axis-title" x="598" y="762" text-anchor="middle" textLength="408" lengthAdjust="spacing">Years Since Diagnosis</text>
  <text class="axis-title" transform="translate(123 430) rotate(-90)" text-anchor="middle" textLength="122" lengthAdjust="spacing">SWI-TC</text>
  <text class="side-title" transform="translate(1073 426) rotate(90)" text-anchor="middle" textLength="264" lengthAdjust="spacing">Quality of Life</text>
</svg>
</body>
</html>
```